KOR Design

Looking for the website design of an small business,
The company is newly established. The Company Trades with Steel from Asiam Europe to Australia and New Zealand.

In the main Page, we would like to have a video showing the process of how steel is made(or the iron melt, pipe rolled, etc)

We would like to show pictures of the Products we trade and an table with some information about the specifications and Product.

About the company,
Industry is Iron and Steel
The company source and supply various steel and metal products within our international network also manage all aspects of the supply process from point of manufacture to point of delivery. the goal is to create value within the supply chain by building strong supplier, customers and service providers, funding of both customers and suppliers, experienced risk management, efficient document handling.
Main products: LSAW pipe, ERW Pipe, Flat rolled Products (such is Steel Coil, Aluminium Zinc Coil, Floor Plate, Plate, etc), Reinforcing bar

Number of Pages Required

5+ page

Font styles to use
Sans Serif

Requirements
Must have
• Video in the home page showing

```html
<!DOCTYPE html>
<html lang="en">
<head>
<meta charset="utf-8">
<title>KOR Design – Steel Trading</title>
<link href="https://fonts.googleapis.com/css2?family=Rubik:wght@400;500;700&display=swap" rel="stylesheet">
<style>
:root{
  --navy:#0f2546;
  --orange:#f15a22;
  --light:#ebebeb;
  --slate:#6b6d72;
  --footer:#1b1c1f;
  --text:#3a3a3a;
  --white:#fff;
}
*{box-sizing:border-box;margin:0;padding:0}
html,body{width:1200px;height:4335px;overflow:hidden}
body{font-family:"Rubik",sans-serif;color:var(--text);background:var(--white);position:relative}
.abs{position:absolute}
section,header,footer{position:absolute;left:0;width:1200px}

/* header */
.site-header{top:0;height:123px;background:var(--white)}
.brand-box{left:130px;top:0;width:196px;height:160px;background:var(--white);z-index:3;display:flex;align-items:center;justify-content:center;gap:10px}
.brand-box .dot{width:18px;height:18px;border-radius:50%;background:var(--orange)}
.brand-box .name{font-weight:700;font-size:24px;color:var(--navy)}
.call{left:734px;top:20px;display:flex;gap:12px;align-items:center}
.call small{display:block;font-size:12px;font-weight:500;color:var(--navy)}
.call strong{font-size:17px;color:var(--orange);font-weight:500}
.socials{display:flex;gap:12px}
.socials span{width:30px;height:30px;border:2px solid var(--orange);border-radius:50%;display:block}
.site-header .socials{position:absolute;left:947px;top:22px}
.nav{position:absolute;left:545px;top:80px;display:flex;gap:33px;font-size:15px;font-weight:700;color:var(--navy)}

/* hero */
.hero{top:123px;height:643px;background:radial-gradient(circle at 30% 30%,#c55a1c 0%,#6a2a10 45%,#1e0d07 100%)}
.hero h1{position:absolute;left:216px;top:170px;font-size:64px;line-height:72px;font-weight:700;color:var(--white)}
.hero p{position:absolute;left:216px;top:320px;width:420px;font-size:21px;line-height:33px;color:var(--white)}
.btn-ghost{position:absolute;left:226px;top:415px;width:196px;height:54px;border:3px solid var(--white);border-radius:30px;color:var(--white);font-weight:700;font-size:18px;display:flex;align-items:center;justify-content:center}
.arrow{position:absolute;width:72px;height:72px;border:3px solid var(--white);border-radius:50%;display:flex;align-items:center;justify-content:center}
.dots{position:absolute;left:565px;top:570px;display:flex;gap:10px}
.dots span{width:18px;height:18px;border-radius:50%;border:2px solid var(--white)}
.dots span.on{background:var(--white);border-color:var(--orange)}

/* about */
.about{top:766px;height:534px}
.about-visual{left:135px;top:50px;width:370px;height:426px;border-radius:50%;background:radial-gradient(circle,#d96a22 0%,#8a3510 45%,rgba(255,255,255,0) 72%)}
.about h2{position:absolute;left:589px;top:80px;font-size:40px;line-height:48px;font-weight:700;color:var(--navy)}
.about h2 em{font-style:normal;color:var(--orange)}
.about .rule{position:absolute;left:1038px;top:104px;width:162px;border-top:2px dashed var(--orange)}
.about .rule::before{content:"";position:absolute;left:-6px;top:-7px;width:12px;height:12px;border-radius:50%;background:var(--orange)}
.about p{position:absolute;left:589px;width:460px;font-size:16.5px;line-height:26px}
.btn-outline{position:absolute;height:48px;border:3px solid var(--navy);border-radius:26px;color:var(--navy);font-weight:500;font-size:16px;display:flex;align-items:center;justify-content:center}

/* values */
.values{top:1300px;height:644px;background:var(--light)}
.values .tab{position:absolute;left:550px;top:-34px;width:100px;height:100px;border-radius:50%;background:var(--light)}
.oct{position:absolute;width:249px;height:249px;background:var(--navy);clip-path:polygon(30% 0,70% 0,100% 30%,100% 70%,70% 100%,30% 100%,0 70%,0 30%);color:var(--white);text-align:center;font-size:20px;line-height:26px;display:flex;flex-direction:column;align-items:center;justify-content:center;gap:12px}
.oct.hot{background:var(--orange)}
.oct .ico{width:52px;height:52px}
.oct .chev{width:34px;height:34px;border:2px solid var(--white);border-radius:50%;display:flex;align-items:center;justify-content:center}

/* products */
.products{top:1944px;height:598px}
.title{position:absolute;left:0;width:1200px;text-align:center;font-size:40px;font-weight:700;color:var(--navy)}
.title em{font-style:normal;color:var(--orange)}
.product{position:absolute;top:140px;width:214px;height:318px}
.card{position:absolute;left:377px;top:140px;width:214px;height:367px;background:var(--white);box-shadow:0 8px 22px rgba(0,0,0,.18);text-align:center}
.card .img{height:270px;background:linear-gradient(180deg,#8a949c,#2e3338)}
.card h3{font-size:19px;font-weight:500;color:#111;margin-top:18px}
.card p{font-size:13px;line-height:18px;margin-top:4px}
.nav-dot{position:absolute;top:2220px;width:44px;height:44px;border-radius:50%;background:var(--navy);display:flex;align-items:center;justify-content:center}

/* who */
.who{top:2542px;height:552px;background:var(--navy);color:var(--white)}
.who .photo{position:absolute;left:615px;top:0;width:585px;height:552px;background:linear-gradient(135deg,#5d6b78,#2b333c 50%,#a8462a);clip-path:ellipse(100% 78% at 100% 50%)}
.who .line{position:absolute;left:0;top:133px;width:105px;border-top:2px dashed var(--white)}
.who .line::after{content:"";position:absolute;right:-6px;top:-7px;width:12px;height:12px;border-radius:50%;background:var(--white)}
.who h2{position:absolute;left:131px;top:116px;font-size:27px;font-weight:700}
.who p{position:absolute;left:131px;top:170px;width:420px;font-size:16px;line-height:25px}
.who ul{position:absolute;left:131px;top:263px;list-style:none}
.who li{display:flex;align-items:center;gap:16px;font-size:15px;font-weight:500;height:38px;letter-spacing:.4px}

/* why */
.why{top:3094px;height:424px;background:var(--slate);color:var(--white);text-align:center}
.why .stem{position:absolute;left:599px;top:-22px;height:50px;border-left:2px dashed var(--white)}
.why .stem::after{content:"";position:absolute;left:-7px;bottom:-6px;width:12px;height:12px;border-radius:50%;background:var(--white)}
.why h2{position:absolute;left:0;width:1200px;top:80px;font-size:29px;font-weight:700}
.feature{position:absolute;top:142px;width:220px}
.feature .ring{width:94px;height:94px;margin:0 auto;border:3px solid var(--white);border-radius:50%;display:flex;align-items:center;justify-content:center}
.feature h3{font-size:21px;font-weight:400;margin-top:24px}
.feature p{font-size:13px;line-height:19px;margin-top:10px}

/* contact */
.contact{top:3518px;height:475px}
.field{position:absolute;width:314px;height:47px;border:1.5px solid #bdbdbd;padding:0 18px;font-size:17px;color:#555;display:flex;align-items:center}

/* footer */
.site-footer{top:3993px;height:342px;background:var(--footer);color:var(--white)}
.col{position:absolute;top:62px}
.col h4{font-size:21px;font-weight:500;margin-bottom:14px}
.col li{list-style:none;font-size:15px;line-height:27px}
.contact-row{display:flex;gap:10px;align-items:center;font-size:15px;line-height:19px;margin-bottom:16px}
.foot-brand{position:absolute;left:870px;top:80px;display:flex;gap:10px;align-items:center}
.foot-brand .name{font-size:30px;font-weight:700}
.foot-brand .dot{width:20px;height:20px;border-radius:50%;background:var(--orange)}
.site-footer .socials{position:absolute;left:883px;top:196px;gap:8px}
.site-footer .socials span{width:32px;height:32px;border-color:var(--white)}
.copy{position:absolute;left:0;top:265px;width:1200px;border-top:1px solid #3a3b40;text-align:center;padding-top:22px;font-size:14px}
</style>
</head>
<body>

<header class="site-header">
  <div class="abs brand-box"><span class="dot"></span><span class="name">KOR Design</span></div>
  <div class="abs call">
    <svg width="32" height="32" viewBox="0 0 24 24" fill="none" stroke="#0f2546" stroke-width="1.6"><path d="M5 3h4l2 5-3 2a11 11 0 0 0 6 6l2-3 5 2v4a2 2 0 0 1-2 2A17 17 0 0 1 3 5a2 2 0 0 1 2-2z"/></svg>
    <div><small>CALL US</small><strong>+1 555 010 2040</strong></div>
  </div>
  <div class="socials"><span></span><span></span><span></span></div>
  <nav class="nav"><span>HOME</span><span>OUR PRODUCTS</span><span>ABOUT US</span><span>NEWS</span><span>CONTACT US</span></nav>
</header>

<section class="hero" role="img" aria-label="Video of molten steel being poured in a foundry by a worker">
  <h1>KOR DESIGN<br>STEEL TRADERS</h1>
  <p>Lorem Ipsum is simply dummy text of the printing and typesetting industry</p>
  <div class="btn-ghost">LEARN MORE</div>
  <div class="arrow" style="left:82px;top:265px"><svg width="22" height="30" viewBox="0 0 22 30"><path d="M16 3 4 15l12 12" fill="none" stroke="#fff" stroke-width="4"/></svg></div>
  <div class="arrow" style="left:1044px;top:265px"><svg width="22" height="30" viewBox="0 0 22 30"><path d="M6 3l12 12L6 27" fill="none" stroke="#fff" stroke-width="4"/></svg></div>
  <div class="dots"><span></span><span class="on"></span><span></span></div>
</section>

<section class="about">
  <div class="abs about-visual" role="img" aria-label="Sunburst-framed photo of molten metal"></div>
  <h2>ABOUT <em>KOR DESIGN<br>STEEL TRADERS</em></h2>
  <div class="rule"></div>
  <p style="top:192px">Lorem Ipsum is simply dummy text of the printing and typesetting industry. Lorem Ipsum has been</p>
  <p style="top:258px">industry's standard dummy text ever since the 1500s, when an unknown printer took a galley of type and scrambled Lorem Ipsum is simply dummy text of the printing and typesetting industry.</p>
  <div class="btn-outline" style="left:589px;top:382px;width:168px">LEARN MORE</div>
</section>

<section class="values">
  <div class="tab"></div>
  <div class="oct" style="left:203px;top:91px">
    <svg class="ico" viewBox="0 0 52 52" fill="none" stroke="#fff" stroke-width="2"><circle cx="26" cy="26" r="6"/><circle cx="10" cy="10" r="5"/><circle cx="42" cy="10" r="5"/><circle cx="10" cy="42" r="5"/><circle cx="42" cy="42" r="5"/><path d="M14 14l8 8M38 14l-8 8M14 38l8-8M38 38l-8-8"/></svg>
    <div>Building Strong<br>Supplier</div><div class="chev"><svg width="14" height="10"><path d="M1 2l6 6 6-6" fill="none" stroke="#fff" stroke-width="2"/></svg></div>
  </div>
  <div class="oct hot" style="left:476px;top:91px">
    <svg class="ico" viewBox="0 0 52 52" fill="none" stroke="#fff" stroke-width="2"><circle cx="30" cy="12" r="6"/><path d="M20 30c0-6 4-10 10-10s10 4 10 10z"/><path d="M4 34l10-4h12l-12 12H6z"/></svg>
    <div>Customers &amp;<br>Service Providers</div><div class="chev"><svg width="14" height="10"><path d="M1 2l6 6 6-6" fill="none" stroke="#fff" stroke-width="2"/></svg></div>
  </div>
  <div class="oct" style="left:748px;top:91px">
    <svg class="ico" viewBox="0 0 52 52" fill="none" stroke="#fff" stroke-width="2"><circle cx="28" cy="18" r="10"/><path d="M28 12v12M25 15h5M25 21h5"/><path d="M4 40l10-6h14l-10 10H6z"/></svg>
    <div>Funding of Customers<br>&amp; Suppliers</div><div class="chev"><svg width="14" height="10"><path d="M1 2l6 6 6-6" fill="none" stroke="#fff" stroke-width="2"/></svg></div>
  </div>
  <div class="oct" style="left:339px;top:303px">
    <svg class="ico" viewBox="0 0 52 52" fill="none" stroke="#fff" stroke-width="2"><circle cx="26" cy="14" r="7"/><circle cx="14" cy="34" r="7"/><circle cx="38" cy="34" r="7"/></svg>
    <div>Experienced<br>Risk Management</div><div class="chev"><svg width="14" height="10"><path d="M1 2l6 6 6-6" fill="none" stroke="#fff" stroke-width="2"/></svg></div>
  </div>
  <div class="oct" style="left:611px;top:303px">
    <svg class="ico" viewBox="0 0 52 52" fill="none" stroke="#fff" stroke-width="2"><path d="M12 4h24l6 6v38H12z"/><circle cx="26" cy="20" r="7"/><path d="M18 34h16M18 40h16"/></svg>
    <div>Efficient<br>Document Handling</div><div class="chev"><svg width="14" height="10"><path d="M1 2l6 6 6-6" fill="none" stroke="#fff" stroke-width="2"/></svg></div>
  </div>
</section>

<section class="products">
  <h2 class="title" style="top:55px">OUR <em>PRODUCTS</em></h2>
  <div class="product" style="left:146px;background:linear-gradient(180deg,#f2f2f2 40%,#3b4148)" role="img" aria-label="LSAW pipes stacked outdoors"></div>
  <div class="card">
    <div class="img" role="img" aria-label="Stacked ERW steel pipes"></div>
    <h3>ERW PIPE</h3>
    <p>Lorem Ipsum is<br>simply dummy text</p>
  </div>
  <div class="product" style="left:608px;background:linear-gradient(160deg,#9aa3aa,#30363c)" role="img" aria-label="Rolled steel coils in a warehouse"></div>
  <div class="product" style="left:840px;background:linear-gradient(160deg,#6f7479,#1f2326)" role="img" aria-label="Bundles of reinforcing bar"></div>
</section>
<div class="nav-dot" style="left:69px"><svg width="10" height="14"><path d="M8 1 2 7l6 6" fill="none" stroke="#fff" stroke-width="2"/></svg></div>
<div class="nav-dot" style="left:1087px"><svg width="10" height="14"><path d="M2 1l6 6-6 6" fill="none" stroke="#fff" stroke-width="2"/></svg></div>

<section class="who">
  <div class="photo" role="img" aria-label="Stacks of steel pipes with orange caps"></div>
  <div class="line"></div>
  <h2>WHO WE ARE</h2>
  <p>Lorem Ipsum is simply dummy text of the printing and typesetting industry. Lorem Ipsum has been the industry's standard dummy text ever since the 1500s</p>
  <ul>
    <li><svg width="24" height="24" viewBox="0 0 24 24" fill="none" stroke="#fff" stroke-width="2"><circle cx="12" cy="12" r="10"/><path d="M7 12l4 4 8-9"/></svg>LOREM IPSUM IS SIMPLY DUMMY</li>
    <li><svg width="24" height="24" viewBox="0 0 24 24" fill="none" stroke="#fff" stroke-width="2"><circle cx="12" cy="12" r="10"/><path d="M7 12l4 4 8-9"/></svg>LOREM IPSUM IS</li>
    <li><svg width="24" height="24" viewBox="0 0 24 24" fill="none" stroke="#fff" stroke-width="2"><circle cx="12" cy="12" r="10"/><path d="M7 12l4 4 8-9"/></svg>LOREM IPSUM IS SIMPLY</li>
    <li><svg width="24" height="24" viewBox="0 0 24 24" fill="none" stroke="#fff" stroke-width="2"><circle cx="12" cy="12" r="10"/><path d="M7 12l4 4 8-9"/></svg>LOREM IPSUM IS SIMPLY DUMMY</li>
  </ul>
</section>

<section class="why">
  <div class="stem"></div>
  <h2>WHY CHOOSE US</h2>
  <div class="feature" style="left:202px">
    <div class="ring"><svg width="44" height="44" viewBox="0 0 44 44" fill="none" stroke="#fff" stroke-width="3"><circle cx="27" cy="17" r="11"/><path d="M19 25 6 38"/></svg></div>
    <h3>Professionalism</h3><p>Use our body field scanner, at home to uncover why you feel the way you do</p>
  </div>
  <div class="feature" style="left:496px">
    <div class="ring"><svg width="44" height="44" viewBox="0 0 44 44" fill="none" stroke="#fff" stroke-width="3"><circle cx="22" cy="22" r="16"/><path d="M14 22l7 7 16-17"/></svg></div>
    <h3>Better Results</h3><p>Use our body field scanner, at home to uncover why you feel the way you do</p>
  </div>
  <div class="feature" style="left:777px">
    <div class="ring"><svg width="44" height="44" viewBox="0 0 44 44" fill="none" stroke="#fff" stroke-width="3"><circle cx="10" cy="10" r="4"/><circle cx="34" cy="34" r="4"/><path d="M14 10h16a6 6 0 0 1 0 12H14a6 6 0 0 0 0 12h16"/></svg></div>
    <h3>Quality Work</h3><p>Use our body field scanner, at home to uncover why you feel the way you do</p>
  </div>
</section>

<section class="contact">
  <h2 class="title" style="top:55px">GET IN <em>TOUCH</em></h2>
  <div class="field" style="left:273px;top:134px">Your Name</div>
  <div class="field" style="left:613px;top:134px">Subject</div>
  <div class="field" style="left:273px;top:206px">Email Address</div>
  <div class="field" style="left:613px;top:206px;height:118px"></div>
  <div class="field" style="left:273px;top:279px">Phone</div>
  <div class="btn-outline" style="left:515px;top:361px;width:168px;border-color:var(--orange)">LEARN MORE</div>
</section>

<footer class="site-footer">
  <div class="col" style="left:131px"><h4>COMPANY</h4><ul><li>Home</li><li>About Us</li><li>Products</li><li>Services</li><li>Support</li></ul></div>
  <div class="col" style="left:350px"><h4>RESOURCES</h4><ul><li>Testimonials</li><li>Sitemap</li><li>Career</li><li>Contact Us</li><li>Tearms</li></ul></div>
  <div class="col" style="left:567px"><h4>CONTACT US</h4>
    <div class="contact-row"><svg width="14" height="18" viewBox="0 0 14 18"><path d="M7 1a6 6 0 0 1 6 6c0 4-6 10-6 10S1 11 1 7a6 6 0 0 1 6-6z" fill="#fff"/><circle cx="7" cy="7" r="2" fill="#1b1c1f"/></svg><span>42 Harbour Lane #7<br>Perth WA 6000</span></div>
    <div class="contact-row"><svg width="16" height="16" viewBox="0 0 24 24"><path d="M5 3h4l2 5-3 2a11 11 0 0 0 6 6l2-3 5 2v4a2 2 0 0 1-2 2A17 17 0 0 1 3 5a2 2 0 0 1 2-2z" fill="#fff"/></svg><span>(555) 010 2040</span></div>
    <div class="contact-row"><svg width="16" height="12" viewBox="0 0 16 12"><rect x="1" y="1" width="14" height="10" fill="none" stroke="#fff" stroke-width="1.5"/><path d="M1 1l7 6 7-6" fill="none" stroke="#fff" stroke-width="1.5"/></svg><span>info@kordesign.example</span></div>
  </div>
  <div class="foot-brand"><span class="dot"></span><span class="name">KOR Design</span></div>
  <div class="socials"><span></span><span></span><span></span><span></span></div>
  <div class="copy">© 2020 KOR Design. All Rights are Reserved.</div>
</footer>

</body>
</html>
```